Modern Venture Capital website

Design a modern website for a venture capital firm. This website should be modern and beautiful and be on par with other Venture Capital websites. I have a logo and a hero video I'd like to use. Link to hero video: https://files.vantoria.example/f/9Xk2Lm7qPz4Rt8Wb3Nc6Hd5Jy1Gs0Ve/view?ref=share_link

Preference will be given to the best design that combines design with the best images and digital content. That means no generic free stock videos 😅

I currently built a wix website to give you an idea of what content needs to be on the website. Depending on your design it can be 3 pages, or one long page. I will leave it up to you.

WEBSITE: https://brelmor58204.pagecraftly.example/my-site-4

Target Market(s)

Mid-career professionals, individuals interested in Venture Capital

Industry/Entity Type

Finance, venture capital, startups

Requirements
Must have
• must use the hero video I have and must use my logo. Must use high quality images that matches the website design - no generic stock images

```html
<!DOCTYPE html>
<html lang="en">
<head>
<meta charset="utf-8">
<title>Lateshift Ventures</title>
<link rel="stylesheet" href="https://fonts.googleapis.com/css2?family=Inter:wght@400;500;600;700&display=swap">
<style>
:root{
  --page:#ffffff;
  --ink:#ffffff;
  --muted:#9a9a9a;
  --dim:#bdbdbd;
  --base:#0b0b0b;
  --panel:#111111;
  --card-top:#2b2b2b;
  --card-bottom:#141414;
  --accent:#f0532c;
  --ember-dark:#150300;
  --ember:#3a1206;
}
*{margin:0;padding:0;box-sizing:border-box}
html,body{width:1200px;height:1200px;overflow:hidden;background:var(--page)}
body{font-family:'Inter',sans-serif;color:var(--ink);position:relative}
.site{position:absolute;left:427px;top:83px;width:556px;height:1665px;background:var(--base);transform:scale(.6211);transform-origin:0 0;overflow:hidden}
.abs{position:absolute}
.brand{font-weight:700;font-size:11px;letter-spacing:-.2px;color:var(--ink)}

/* nav */
.nav{left:0;top:0;width:556px;height:39px}
.nav .brand{left:17px;top:12px}
.nav-links{left:90px;top:16px;display:flex;gap:16px;font-size:5px}
.login{left:436px;top:14px;display:flex;align-items:center;gap:6px;font-size:5px}
.login i{width:11px;height:11px;border:1px solid var(--ink);border-radius:50%;display:block}
.btn-light{left:492px;top:12px;width:48px;height:15px;background:#e9e9e9;color:#111;border-radius:3px;font-size:5px;font-weight:600;display:flex;align-items:center;justify-content:center}

/* hero */
.hero{left:15px;top:39px;width:525px;height:309px;border-radius:8px;overflow:hidden;
  background:radial-gradient(ellipse 70% 45% at 55% 85%,#5a3a18 0%,#2a1a0a 45%,transparent 80%),linear-gradient(#050505 0%,#0a0806 45%,#1e140a 80%,#2a1c0e 100%)}
.hero h1{left:23px;top:58px;font-size:30px;line-height:35px;font-weight:600;letter-spacing:-.3px;width:320px}
.hero .sub{left:23px;top:166px;font-size:15px}
.btn{background:var(--accent);color:#fff;border-radius:3px;font-size:7px;font-weight:600;display:flex;align-items:center;justify-content:center}
.hero .btn{left:23px;top:204px;width:66px;height:21px}

/* features */
.intro{left:15px;top:364px;width:218px;height:347px;border-radius:6px;overflow:hidden;background:#000}
.intro .trails{left:0;top:180px;width:218px;height:167px;background:radial-gradient(ellipse 90% 70% at 10% 5%,#ffffff 0%,#c8452a 18%,#5a1408 45%,transparent 80%)}
.intro h2{left:23px;top:24px;font-size:18px;font-weight:700}
.intro p{left:23px;top:52px;width:160px;font-size:8.5px;line-height:11px;color:var(--dim)}
.card{width:145px;height:169px;border-radius:6px;border:1px solid #3a3a3a;background:linear-gradient(var(--card-top),var(--card-bottom))}
.card .icon{left:15px;top:15px;width:28px;height:28px;border-radius:50%;background:linear-gradient(#6a6a6a,#3a3a3a);display:flex;align-items:center;justify-content:center}
.card h3{left:15px;top:72px;font-size:12px;line-height:15px;font-weight:600}
.card p{left:15px;top:105px;width:115px;font-size:8.5px;line-height:11px;color:var(--muted)}

/* founders */
.founders{left:0;top:727px;width:556px;height:270px;background:var(--panel)}
.founders .art{left:0;top:0;width:255px;height:270px;background:radial-gradient(ellipse 45% 55% at 40% 45%,#3a1208 0%,#1a0805 50%,#000 85%)}
.founders h2{left:287px;top:58px;font-size:18px;line-height:23px;font-weight:600;width:220px}
.founders p{left:287px;top:112px;width:202px;font-size:8.5px;line-height:12.4px;color:var(--dim);text-align:justify}
.founders .btn{left:287px;top:190px;width:67px;height:22px}

/* economics */
.economics{left:0;top:997px;width:556px;height:155px;background:linear-gradient(180deg,var(--ember-dark),var(--ember))}
.economics h2{left:0;top:35px;width:556px;text-align:center;font-size:18px;font-weight:600}
.stat{top:78px;width:100px;text-align:center;margin-left:-50px}
.stat b{display:block;font-size:24px;font-weight:500;line-height:30px}
.stat span{display:block;font-size:9px;line-height:11px;color:#ddd}
.divider{top:86px;width:1px;height:28px;background:#9a8a85}

/* partners */
.partners{left:0;top:1152px;width:556px;height:132px;background:var(--base)}
.partners h2{left:0;top:31px;width:556px;text-align:center;font-size:18px;font-weight:600}
.partner{top:76px;width:100px;margin-left:-50px;text-align:center;font-size:14px;font-weight:700;color:#8a8a8a}

/* cta */
.cta{left:0;top:1284px;width:556px;height:233px;background:var(--base)}
.cta .left{left:0;top:0;width:309px;height:233px;background:#141414;overflow:hidden}
.cta .glow{left:2px;top:23px;width:306px;height:306px;border-radius:50%;background:linear-gradient(180deg,#d2581c 0%,#7a2c0c 35%,#2a140c 60%,#141414 80%)}
.cta h2{left:38px;top:132px;font-size:25px;line-height:25px;font-weight:500;width:260px;letter-spacing:-.3px}
.cta .note{left:332px;top:87px;width:200px;text-align:center;font-size:8.5px;line-height:11.5px}
.cta .btn{left:403px;top:123px;width:59px;height:21px}

/* footer */
.footer{left:0;top:1517px;width:556px;height:148px;background:var(--base);border-top:1px solid #1a1a1a}
.footer .brand{left:17px;top:38px}
.footer .info{left:15px;top:62px;font-size:5px;line-height:6px;color:var(--dim)}
.socials{left:15px;top:93px;display:flex;gap:6px}
.socials i{display:block;width:7px;height:7px;border-radius:50%;background:#8a8a8a}
.copy{left:15px;top:111px;font-size:5px;color:var(--dim)}
.col{top:37px;font-size:5px;line-height:11.5px;color:var(--muted)}
.col b{color:var(--ink);font-weight:500}
.email{left:449px;top:59px;width:91px;height:11px;border:1px solid #555;border-radius:2px}
.submit{left:449px;top:84px;width:36px;height:11px;background:#fff;color:#111;font-size:5px;font-weight:600;border-radius:2px;display:flex;align-items:center;justify-content:center}
</style>
</head>
<body>
<div class="site">
  <header class="nav abs">
    <div class="brand abs">Lateshift</div>
    <nav class="nav-links abs"><span>Home</span><span>Join VC</span><span>Startups</span><span>Contact</span></nav>
    <div class="login abs"><i></i><span>Log In</span></div>
    <div class="btn-light abs">Get Started</div>
  </header>

  <section class="hero abs" role="img" aria-label="Night view over a city skyline with glowing lights">
    <h1 class="abs">Venture Capital For The Late Night Hustlers</h1>
    <div class="sub abs">Become a Venture Capital Investor</div>
    <div class="btn abs">Learn More</div>
  </section>

  <section class="intro abs">
    <div class="trails abs" role="img" aria-label="Long exposure light trails of traffic at night"></div>
    <h2 class="abs">Become a VC</h2>
    <p class="abs">Join a new wave of investors who don’t just watch they build, decide, and grow.</p>
  </section>

  <article class="card abs" style="left:243px;top:364px">
    <div class="icon abs"><svg width="12" height="12" viewBox="0 0 12 12" fill="none" stroke="#fff" stroke-width="1"><path d="M2 10l5-5M7 5a2.5 2.5 0 1 0 2-3l-1.5 1.5 1 1L10 3a2.5 2.5 0 0 1-3 2z"/></svg></div>
    <h3 class="abs">Hands On<br>VC Work</h3>
    <p class="abs">Get involved in sourcing, evaluating, and making investment decisions.</p>
  </article>
  <article class="card abs" style="left:396px;top:364px">
    <div class="icon abs"><svg width="12" height="12" viewBox="0 0 12 12" fill="none" stroke="#fff" stroke-width="1"><path d="M1.5 1.5h4.5l4.5 4.5-4.5 4.5-4.5-4.5z"/><circle cx="4" cy="4" r=".8"/></svg></div>
    <h3 class="abs">Earn Carry &amp;<br>Get Credited</h3>
    <p class="abs">Earn a share of returns based on your role in each deal.</p>
  </article>
  <article class="card abs" style="left:243px;top:541px">
    <div class="icon abs"><svg width="12" height="12" viewBox="0 0 12 12" fill="none" stroke="#fff" stroke-width="1"><path d="M1 11h10M2 11V7h2v4M5 11V5h2v6M8 11V2h2v9"/></svg></div>
    <h3 class="abs">Advance Your<br>VC Career</h3>
    <p class="abs">Grow into roles like Partner, Associate, or Venture Partner.</p>
  </article>
  <article class="card abs" style="left:396px;top:541px">
    <div class="icon abs"><svg width="12" height="12" viewBox="0 0 12 12" fill="none" stroke="#fff" stroke-width="1"><circle cx="6" cy="6" r="5"/><ellipse cx="6" cy="6" rx="2.2" ry="5"/><path d="M1 6h10"/></svg></div>
    <h3 class="abs">Join a Driven<br>Community</h3>
    <p class="abs">Connect with investors, founders, and ambitious professionals.</p>
  </article>

  <section class="founders abs">
    <div class="art abs" role="img" aria-label="Abstract artwork of translucent red and white geometric shapes"></div>
    <h2 class="abs">Simplifying Success For Founders</h2>
    <p class="abs">Our LPs and operating partners are senior industry executives who provide strategic guidance and operational support to help our portfolio companies grow. We make decisions promptly with transparency and respect.</p>
    <div class="btn abs">Learn More</div>
  </section>

  <section class="economics abs">
    <h2 class="abs">Fund Economics</h2>
    <div class="stat abs" style="left:52px"><b>14</b><span>Pre-Seed/Seed<br>Investments</span></div>
    <div class="divider abs" style="left:109px"></div>
    <div class="stat abs" style="left:165px"><b>50K</b><span>Check Size</span></div>
    <div class="divider abs" style="left:222px"></div>
    <div class="stat abs" style="left:278px"><b>20%</b><span>Carried Interest</span></div>
    <div class="divider abs" style="left:334px"></div>
    <div class="stat abs" style="left:390px"><b>2.5%</b><span>Management Fee</span></div>
    <div class="divider abs" style="left:447px"></div>
    <div class="stat abs" style="left:503px"><b>1M</b><span>Fund Size</span></div>
  </section>

  <section class="partners abs">
    <h2 class="abs">Our Partners</h2>
    <div class="partner abs" style="left:97px">Korvan</div>
    <div class="partner abs" style="left:221px">Ashfield</div>
    <div class="partner abs" style="left:348px">Tenmora</div>
    <div class="partner abs" style="left:472px">Quillo</div>
  </section>

  <section class="cta abs">
    <div class="left abs">
      <div class="glow abs"></div>
      <h2 class="abs">Invest with purpose. Join the next wave of VCs.</h2>
    </div>
    <p class="note abs">Schedule a conversation to learn more and check your eligibility.</p>
    <div class="btn abs">Let’s Talk</div>
  </section>

  <footer class="footer abs">
    <div class="brand abs">Lateshift</div>
    <div class="info abs">(406) 555-0177<br><br>418 Harlow Ave. Brenton,<br>Ohio 44120</div>
    <div class="socials abs" aria-label="Social links"><i></i><i></i><i></i></div>
    <div class="copy abs">© 2025 by Lateshift Ventures</div>
    <div class="col abs" style="left:160px"><b>Company</b><br>About<br>Careers<br>Press</div>
    <div class="col abs" style="left:256px"><b>Resources</b><br>Blog<br>Case Studies<br>Guides</div>
    <div class="col abs" style="left:353px"><b>Contact</b><br>Email Us<br>Support</div>
    <div class="col abs" style="left:449px"><b>Subscribe to Our Newsletter</b><br>Email</div>
    <div class="email abs"></div>
    <div class="submit abs">Submit</div>
  </footer>
</div>
</body>
</html>
```